Metal Recycling Website Require New Design for upgrade

Our company currently have an existing website, www.tovarekmetals.com and the website is generally outdated so we would like an improvement.

We would generally prefer to keep the current color theme of our website as it is similar to our current logo.

We would also like our company factory picture to be on somewhere of the webpage (but only if the designer think that the picture can blend well with the color theme)

Our company is dealing alot Aluminiun, Stainless Steel, Copper, Brass, Iron

Pictures uploaded.

Target Market(s)

General Commercial Manufacturer, B2B

Industry/Entity Type

Recycling

Number of Pages Required

1 page

Colors

Designer to choose colors to be used in the design.

Requirements
Must have
• Hopefully color will be similar to my logo theme but designer welcome to have their own input.
Nice to have
• Company Picture (Uploaded in the file)

```html
<!DOCTYPE html>
<html lang="en">
<head>
<meta charset="utf-8">
<title>Tovarek Metals</title>
<link rel="stylesheet" href="https://fonts.googleapis.com/css2?family=Catamaran:wght@300;400;500;600;700&family=Montserrat:wght@800&family=Poppins:wght@500&display=swap">
<style>
:root{
  --gold:#d49a0c;
  --gold-light:#e2b54a;
  --ink:#111111;
  --body:#6b6b6b;
  --light-bg:#f4f4f4;
  --footer:#1b1b1b;
  --footer-text:#9a9a9a;
  --white:#ffffff;
}
*{margin:0;padding:0;box-sizing:border-box}
html,body{width:1200px;height:2688px;overflow:hidden;background:var(--white)}
body{position:relative;font-family:"Catamaran",sans-serif;color:var(--ink)}
.abs{position:absolute}

/* hero */
.hero-photo{left:0;top:0;width:1200px;height:624px;
  background:linear-gradient(180deg,#3a3a3a 0%,#4d4f46 30%,#5b6050 55%,#6f706a 75%,#8a8a88 100%)}
.hero-shape{left:0;top:480px;width:1200px;height:160px}
.contact-line{left:77px;display:flex;align-items:center;gap:16px;color:var(--white);font-size:15px;font-weight:600}
.contact-line svg{width:22px;height:20px}
.brand{display:flex;align-items:center;gap:10px;color:var(--gold);font-weight:700;letter-spacing:1px}
.brand .mark{width:40px;height:40px;border:3px solid var(--gold)}
.brand-head{left:0;width:1200px;top:36px;justify-content:center;font-size:20px}
.menu{right:77px;top:62px;display:flex;align-items:center;gap:12px;color:var(--white);font-size:15px;font-weight:700;letter-spacing:1px}
.menu span.bars{display:flex;flex-direction:column;gap:4px}
.menu span.bars i{display:block;height:2px;background:var(--gold)}
.hero-title{left:0;width:1200px;top:212px;text-align:center;font-family:"Montserrat",sans-serif;font-size:58px;font-weight:800;
  color:#8d8d8d;-webkit-text-stroke:2px var(--white);letter-spacing:1px}
.hero-text{left:190px;width:820px;top:300px;text-align:center;color:var(--white);font-size:16px;line-height:31px}
.btn{display:flex;align-items:center;justify-content:center;background:var(--gold);color:var(--white);border-radius:26px;font-size:16px;font-weight:500;letter-spacing:.5px}
.hero-btn{left:522px;top:386px;width:156px;height:50px}
.scroll-down{left:571px;top:531px;width:58px;height:58px}

/* about */
.frame{border:20px solid var(--gold)}
.about-frame{left:306px;top:718px;width:261px;height:261px;border-left-color:var(--gold-light);border-top-color:var(--gold-light)}
.photo-main{left:153px;top:770px;width:360px;height:360px;background:linear-gradient(160deg,#b7b9bc 0%,#8b7a5e 45%,#5a4a36 75%,#7d7b77 100%);box-shadow:0 2px 8px rgba(0,0,0,.25)}
.photo-small{left:77px;top:1000px;width:208px;height:208px;background:linear-gradient(135deg,#2c2c2e,#5b4a3a 50%,#1f1f20)}
.about-title{left:656px;top:764px;font-size:42px;font-weight:600}
.para{font-size:15px;line-height:27px;color:var(--body);font-weight:300}
.about-p1{left:656px;top:840px;width:440px}
.about-p2{left:656px;top:939px;width:440px}
.about-btn{left:654px;top:1078px;width:156px;height:52px}

/* products */
.products-band{left:0;top:1292px;width:1200px;height:427px}
.products-title{left:80px;top:1368px;font-size:42px;font-weight:600}
.products-p{left:80px;top:1444px;width:560px}
.products-btn{left:77px;top:1584px;width:156px;height:52px}
.prod-frame{left:863px;top:1330px;width:260px;height:260px;border-left-color:var(--gold-light);border-top-color:var(--gold-light)}
.prod-main{left:767px;top:1375px;width:312px;height:260px;background:linear-gradient(135deg,#6a4a36,#8a5a3e 40%,#3b3026 70%,#7a6a5a)}
.prod-s1{left:689px;top:1349px;width:125px;height:105px;background:linear-gradient(135deg,#7b5a44,#c9c5c0 60%,#5a4638)}
.prod-s2{left:715px;top:1574px;width:73px;height:72px;background:linear-gradient(135deg,#3a2e26,#8a6a4e,#4a3a30)}
.prod-badge{left:997px;top:1563px;width:92px;height:92px;background:var(--gold);display:flex;align-items:center;justify-content:center}
.prod-badge i{width:62px;height:62px;border:3px solid var(--white)}

/* services */
.services-title{left:0;width:1200px;top:1796px;text-align:center;font-size:42px;font-weight:600}
.service{width:330px;text-align:center}
.service .icon-wrap{position:relative;width:126px;height:160px;margin:0 auto}
.service .icon{position:absolute;left:11px;top:0;width:104px;height:104px;background:#f7ecd6}
.service .bracket{position:absolute;left:0;top:76px;width:126px;height:40px;border:6px solid var(--gold);border-top:none}
.service .stem{position:absolute;left:60px;top:116px;width:6px;height:44px;background:var(--gold)}
.service h3{margin-top:34px;font-size:20px;font-weight:500;letter-spacing:.5px}
.service p{margin-top:12px;font-size:15px;line-height:27px;color:var(--body);font-weight:300}

/* footer */
.footer{left:0;top:2293px;width:1200px;height:395px;background:var(--footer)}
.brand-foot{left:122px;top:2380px;font-size:22px}
.brand-foot .mark{width:44px;height:44px}
.socials{left:122px;top:2482px;display:flex;gap:8px}
.socials i{width:46px;height:46px;border-radius:50%;background:#3a3a3a;border:2px solid var(--gold)}
.foot-head{top:2352px;font-size:22px;font-weight:500}
.touch-head{left:435px;color:var(--gold);letter-spacing:.5px}
.stay-head{left:719px;color:var(--white);font-family:"Poppins",sans-serif;font-size:20px;top:2354px}
.touch-item{left:435px;display:flex;gap:14px;color:var(--footer-text);font-size:15px;line-height:26px}
.touch-item svg{width:22px;height:22px;flex:none;margin-top:2px}
.stay-text{left:719px;top:2404px;width:330px;color:var(--footer-text);font-size:15px;line-height:27px}
.stay-text b{font-weight:600;color:#c4c4c4}
.subscribe{left:718px;top:2480px;width:405px;height:51px;border:1px solid #555;border-radius:26px;background:#1f1f1f}
.subscribe span{position:absolute;left:22px;top:15px;color:#e0e0e0;font-size:14px}
.subscribe .btn{position:absolute;right:-1px;top:-1px;width:114px;height:51px;font-size:17px}
.footer-rule{left:0;top:2616px;width:1200px;height:1px;background:#333}
.copyright{left:0;width:1200px;top:2642px;text-align:center;color:#666;font-size:13px}
</style>
</head>
<body>

<!-- Hero -->
<div class="abs hero-photo" role="img" aria-label="Scrap yard with piles of aluminium wheel rims, rusted containers and a factory chimney under a dark sky"></div>
<svg class="abs hero-shape" viewBox="0 0 1200 160" preserveAspectRatio="none" aria-hidden="true">
  <polygon points="0,10 600,132 1200,10 1200,160 0,160" fill="#ffffff"/>
  <polygon points="0,10 600,132 1200,10 1200,0 1200,30 600,144 0,30" fill="#d49a0c"/>
  <polygon points="0,0 0,10 600,132 1200,10 1200,0 1200,10 600,132" fill="#d49a0c"/>
</svg>
<svg class="abs" style="left:0;top:488px" width="1200" height="140" viewBox="0 0 1200 140" aria-hidden="true">
  <polygon points="0,0 600,108 1200,0 1200,34 600,136 0,34" fill="#d49a0c"/>
  <polygon points="0,34 600,136 1200,34 1200,140 0,140" fill="#ffffff"/>
</svg>

<div class="abs contact-line" style="top:45px">
  <svg viewBox="0 0 22 16"><rect x="1" y="1" width="20" height="14" fill="none" stroke="#d49a0c" stroke-width="2"/><path d="M1 1l10 8 10-8" fill="none" stroke="#d49a0c" stroke-width="2"/></svg>
  sales@tovarekmetals.com
</div>
<div class="abs contact-line" style="top:77px">
  <svg viewBox="0 0 24 24"><path d="M6.6 10.8a15 15 0 006.6 6.6l2.2-2.2c.3-.3.7-.4 1-.2 1.1.4 2.3.6 3.6.6.6 0 1 .4 1 1V20c0 .6-.4 1-1 1A17 17 0 013 4c0-.6.4-1 1-1h3.5c.6 0 1 .4 1 1 0 1.3.2 2.5.6 3.6.1.3 0 .7-.2 1z" fill="#d49a0c"/></svg>
  +65-6100-2400
</div>
<div class="abs brand brand-head"><span class="mark"></span>TOVAREK METALS</div>
<div class="abs menu">MENU <span class="bars"><i style="width:18px"></i><i style="width:14px"></i><i style="width:18px"></i></span></div>

<h1 class="abs hero-title">LOREM IPSUM DOLOR</h1>
<p class="abs hero-text">Lorem ipsum dolor sit amet, consectetur adipiscing elit, sed do eiusmod tempor incididunt ut labore et dolore consequat. Duis aute irure dolor in reprehenderit in voluptate velit esse cillum dolore eu fugiat nulla pariatur.</p>
<a class="abs btn hero-btn">CONTACT US</a>
<svg class="abs scroll-down" viewBox="0 0 58 58" aria-label="Scroll down">
  <circle cx="29" cy="29" r="27" fill="none" stroke="#ffffff" stroke-width="2"/>
  <path d="M29 19v20M22 32l7 7 7-7" fill="none" stroke="#ffffff" stroke-width="2"/>
</svg>

<!-- About -->
<div class="abs frame about-frame"></div>
<div class="abs photo-small" role="img" aria-label="Close-up of cut copper cable ends"></div>
<div class="abs photo-main" role="img" aria-label="Excavator grab lifting scrap metal in a recycling yard"></div>
<h2 class="abs about-title">ABOUT COMPANY</h2>
<p class="abs para about-p1">Tovarek Metals primary activities are the procurement, pro - cessing, recycling and trading of all ferrous and non-ferrous scrap metals, industrial scraps and other recyclables.</p>
<p class="abs para about-p2">We provide full-service ferrous and non-ferrous metal recycler and processor. Recognized as an industry leader in metal recycling, our team of experienced staff and trader understand the intricacies of scrap metal recycling.</p>
<a class="abs btn about-btn">LEARN MORE</a>

<!-- Products -->
<svg class="abs products-band" viewBox="0 0 1200 427" aria-hidden="true"><polygon points="0,0 887,0 1060,213 887,427 0,427" fill="#f4f4f4"/></svg>
<h2 class="abs products-title">PRODUCTS</h2>
<p class="abs para products-p">Lorem ipsum dolor sit amet, consectetur adipiscing elit, sed do eiusmod tempor incididunt ut labore et dolore magna aliqua. Ut enim ad minim veniam, quis nostrud exercitation ullamco laboris nisi ut aliquip ex ea commodo consequat. Duis aute irure dolor in reprehenderit in voluptate velit esse cillum dolore eu fugiat nulla pariatur.</p>
<a class="abs btn products-btn">LEARN MORE</a>
<div class="abs frame prod-frame"></div>
<div class="abs prod-s1" role="img" aria-label="Pile of scrap metal pipes"></div>
<div class="abs prod-s2" role="img" aria-label="Bundle of scrap metal rods"></div>
<div class="abs prod-main" role="img" aria-label="Heap of scrap copper pipes and fittings"></div>
<div class="abs prod-badge"><i></i></div>

<!-- Services -->
<h2 class="abs services-title">OUR SERVICES</h2>
<div class="abs service" style="left:74px;top:1896px">
  <div class="icon-wrap"><span class="bracket"></span><div class="icon" role="img" aria-label="Icon of a person beside a form"></div><span class="stem"></span></div>
  <h3>FOR INDIVIDUAL</h3>
  <p>We serve the general public mainly by the walk in channel. To serve you better, we have extended our collection hours!</p>
</div>
<div class="abs service" style="left:435px;top:1896px">
  <div class="icon-wrap"><span class="bracket"></span><div class="icon" role="img" aria-label="Icon of office buildings"></div><span class="stem"></span></div>
  <h3>FOR CORPORATE</h3>
  <p>Roll-off Open Top Container (OTC), small container, customized container for the disposal of your scrap material at your premises.</p>
</div>
<div class="abs service" style="left:796px;top:1896px">
  <div class="icon-wrap"><span class="bracket"></span><div class="icon" role="img" aria-label="Icon of a globe with location markers"></div><span class="stem"></span></div>
  <h3>FOR INTERNATIONAL</h3>
  <p>Tovarek Metals have strong relationship with all our international customer, allowing both parties to established long term.</p>
</div>

<!-- Footer -->
<div class="abs footer"></div>
<div class="abs brand brand-foot"><span class="mark"></span>TOVAREK METALS</div>
<div class="abs socials" aria-label="Social links"><i></i><i></i><i></i><i></i></div>

<h3 class="abs foot-head touch-head">GET IN TOUCH</h3>
<div class="abs touch-item" style="top:2414px">
  <svg viewBox="0 0 24 24"><path d="M6.6 10.8a15 15 0 006.6 6.6l2.2-2.2c.3-.3.7-.4 1-.2 1.1.4 2.3.6 3.6.6.6 0 1 .4 1 1V20c0 .6-.4 1-1 1A17 17 0 013 4c0-.6.4-1 1-1h3.5c.6 0 1 .4 1 1 0 1.3.2 2.5.6 3.6.1.3 0 .7-.2 1z" fill="#d49a0c"/></svg>
  +65-6100-2400
</div>
<div class="abs touch-item" style="top:2456px">
  <svg viewBox="0 0 24 24"><rect x="1" y="5" width="22" height="14" fill="#d49a0c"/><path d="M1 5l11 8 11-8" fill="none" stroke="#1b1b1b" stroke-width="2"/></svg>
  sales@tovarekmetals.com
</div>
<div class="abs touch-item" style="top:2502px">
  <svg viewBox="0 0 24 24"><path d="M12 2a7 7 0 00-7 7c0 5 7 13 7 13s7-8 7-13a7 7 0 00-7-7z" fill="#d49a0c"/><circle cx="12" cy="9" r="2.6" fill="#1b1b1b"/></svg>
  <span>18 Foundry Lane,<br>Singapore 700118</span>
</div>

<h3 class="abs foot-head stay-head">Stay connected</h3>
<p class="abs stay-text">Hope on our mailing list to stay up to date on all things <b>TOVAREK METALS</b></p>
<div class="abs subscribe"><span>Enter Email Address</span><a class="btn">SUBCRIBE</a></div>

<div class="abs footer-rule"></div>
<p class="abs copyright">Copyright © TOVAREK METALS - 2019 . All Right Reserved.</p>

</body>
</html>
```